Lumo Tavi Menu Design Project

This project is pretty straight forward. You will be given 3 files which include the following:
1. Our proposed menu
2. Our Company logo
3. A sample menu on what we are looking for design wise

Your job is to create a visually pleasing menu that is simple, clean and fresh. Please refer to our home website for additional information. (www.lumotavi.example) Must be in eps or equivalent format.

Target Market(s)

20s to 40s

Industry/Entity Type

It Company

Requirements
Must have
• Company log
Must be in EPS format

```html
<!DOCTYPE html>
<html lang="en">
<head>
<meta charset="utf-8">
<title>Lumo Tavi Menu</title>
<link href="https://fonts.googleapis.com/css2?family=Alegreya:wght@400;700&family=Arimo:wght@400;700&family=Kaushan+Script&display=swap" rel="stylesheet">
<style>
  :root {
    --bg: #141414;
    --bg-texture: #1b1b1a;
    --red: #d0161c;
    --text: #ffffff;
    --text-soft: #f0f0f0;
  }
  html, body { margin: 0; padding: 0; overflow: hidden; }
  body { width: 927px; height: 1200px; background: var(--bg); }
  .menu {
    position: relative; width: 927px; height: 1200px; overflow: hidden;
    background: radial-gradient(ellipse at 50% 45%, var(--bg-texture), var(--bg) 75%);
    color: var(--text);
  }
  .brand {
    position: absolute; left: 0; width: 927px; top: 44px;
    display: flex; justify-content: center; align-items: center; gap: 8px;
  }
  .brand-mark { width: 14px; height: 14px; background: var(--red); }
  .brand-name {
    font-family: "Alegreya", serif; font-weight: 700; font-size: 30px;
    color: var(--red); line-height: 1;
  }
  .section-title {
    position: absolute; margin: 0;
    font-family: "Kaushan Script", cursive; font-weight: 400;
    font-size: 34px; letter-spacing: 2px; color: var(--red);
    text-transform: uppercase; line-height: 1;
  }
  .title-dimsum { left: 127px; top: 60px; width: 190px; text-align: center; }
  .title-starters { left: 610px; top: 60px; width: 190px; text-align: center; }
  .title-salads { left: 0; width: 927px; top: 968px; text-align: center; }
  .column { position: absolute; top: 155px; width: 396px; }
  .column-left { left: 46px; }
  .column-right { left: 479px; }
  .item { position: relative; height: 91px; }
  .item-name {
    margin: 0; font-family: "Alegreya", serif; font-weight: 400;
    font-size: 23px; line-height: 30px;
  }
  .item-price {
    position: absolute; right: 0; top: 0;
    font-family: "Arimo", sans-serif; font-size: 21px; line-height: 28px;
  }
  .item-desc {
    margin: 0; font-family: "Arimo", sans-serif; font-size: 14px;
    line-height: 18px; color: var(--text-soft);
  }
  .item-featured .item-name, .item-featured .item-desc { font-weight: 700; }
  .salad-note {
    position: absolute; left: 0; width: 927px; top: 1014px; margin: 0;
    text-align: center; font-family: "Arimo", sans-serif; font-size: 13.5px;
  }
  .salad { position: absolute; top: 1062px; width: 272px; }
  .salad-1 { left: 46px; } .salad-2 { left: 334px; } .salad-3 { left: 621px; }
  .salad-head { display: flex; align-items: baseline; gap: 6px; margin-bottom: 6px; }
  .salad-name { margin: 0; font-family: "Alegreya", serif; font-weight: 400; font-size: 21px; }
  .salad-price { font-family: "Arimo", sans-serif; font-size: 19px; }
</style>
</head>
<body>
<main class="menu" role="img" aria-label="Dark menu background with faint floral pattern">
  <div class="brand"><span class="brand-mark"></span><span class="brand-name">Lumo Tavi</span></div>

  <h2 class="section-title title-dimsum">Dim Sum</h2>
  <h2 class="section-title title-starters">Starters</h2>

  <section class="column column-left">
    <div class="item"><h3 class="item-name">Pan-Fried Potstickers</h3><span class="item-price">6.50</span><p class="item-desc">Five pan-Fried potstickers with chicken or pork.<br>Served with apricot dipping sauce.</p></div>
    <div class="item"><h3 class="item-name">Pan-Fried Potstickers</h3><span class="item-price">6.50</span><p class="item-desc">Five pan-Fried potstickers with chicken or pork.<br>Served with apricot dipping sauce.</p></div>
    <div class="item"><h3 class="item-name">Pan-Fried Potstickers</h3><span class="item-price">6.50</span><p class="item-desc">Five pan-Fried potstickers with chicken or pork.<br>Served with apricot dipping sauce.</p></div>
    <div class="item"><h3 class="item-name">Pan-Fried Potstickers</h3><span class="item-price">6.50</span><p class="item-desc">Five pan-Fried potstickers with chicken or pork.<br>Served with apricot dipping sauce.</p></div>
    <div class="item"><h3 class="item-name">Pan-Fried Potstickers</h3><span class="item-price">6.50</span><p class="item-desc">Five pan-Fried potstickers with chicken or pork.<br>Served with apricot dipping sauce.</p></div>
    <div class="item"><h3 class="item-name">Pan-Fried Potstickers</h3><span class="item-price">6.50</span><p class="item-desc">Five pan-Fried potstickers with chicken or pork.<br>Served with apricot dipping sauce.</p></div>
    <div class="item"><h3 class="item-name">Pan-Fried Potstickers</h3><span class="item-price">6.50</span><p class="item-desc">Five pan-Fried potstickers with chicken or pork.<br>Served with apricot dipping sauce.</p></div>
    <div class="item item-featured"><h3 class="item-name">Pan-Fried Potstickers</h3><span class="item-price">6.50</span><p class="item-desc">Five pan-Fried potstickers with chicken or pork.<br>Served with apricot dipping sauce.</p></div>
    <div class="item"><h3 class="item-name">Pan-Fried Potstickers</h3><span class="item-price">6.50</span><p class="item-desc">Five pan-Fried potstickers with chicken or pork.<br>Served with apricot dipping sauce.</p></div>
  </section>

  <section class="column column-right">
    <div class="item"><h3 class="item-name">Pan-Fried Potstickers</h3><span class="item-price">6.50</span><p class="item-desc">Five pan-Fried potstickers with chicken or pork.<br>Served with apricot dipping sauce.</p></div>
    <div class="item"><h3 class="item-name">Pan-Fried Potstickers</h3><span class="item-price">6.50</span><p class="item-desc">Five pan-Fried potstickers with chicken or pork.<br>Served with apricot dipping sauce.</p></div>
    <div class="item"><h3 class="item-name">Pan-Fried Potstickers</h3><span class="item-price">6.50</span><p class="item-desc">Five pan-Fried potstickers with chicken or pork.<br>Served with apricot dipping sauce.</p></div>
    <div class="item"><h3 class="item-name">Pan-Fried Potstickers</h3><span class="item-price">6.50</span><p class="item-desc">Five pan-Fried potstickers with chicken or pork.<br>Served with apricot dipping sauce.</p></div>
    <div class="item"><h3 class="item-name">Pan-Fried Potstickers</h3><span class="item-price">6.50</span><p class="item-desc">Five pan-Fried potstickers with chicken or pork.<br>Served with apricot dipping sauce.</p></div>
    <div class="item"><h3 class="item-name">Pan-Fried Potstickers</h3><span class="item-price">6.50</span><p class="item-desc">Five pan-Fried potstickers with chicken or pork.<br>Served with apricot dipping sauce.</p></div>
    <div class="item"><h3 class="item-name">Pan-Fried Potstickers</h3><span class="item-price">6.50</span><p class="item-desc">Five pan-Fried potstickers with chicken or pork.<br>Served with apricot dipping sauce.</p></div>
    <div class="item item-featured"><h3 class="item-name">Pan-Fried Potstickers</h3><span class="item-price">6.50</span><p class="item-desc">Five pan-Fried potstickers with chicken or pork.<br>Served with apricot dipping sauce.</p></div>
    <div class="item"><h3 class="item-name">Pan-Fried Potstickers</h3><span class="item-price">6.50</span><p class="item-desc">Five pan-Fried potstickers with chicken or pork.<br>Served with apricot dipping sauce.</p></div>
  </section>

  <h2 class="section-title title-salads">Salads</h2>
  <p class="salad-note">Can replace Chicken with Tofu for $1.50</p>

  <div class="salad salad-1"><div class="salad-head"><h3 class="salad-name">Chinese Chicken Salad</h3><span class="salad-price">10.50</span></div><p class="item-desc">Shredded lettuce, chicken breast,<br>scallions, carrots, toasted almonds,<br>browncrunchies, and white crunchies<br>with tart red ginger dressing</p></div>
  <div class="salad salad-2"><div class="salad-head"><h3 class="salad-name">Chinese Chicken Salad</h3><span class="salad-price">10.50</span></div><p class="item-desc">Shredded lettuce, chicken breast,<br>scallions, carrots, toasted almonds,<br>browncrunchies, and white crunchies<br>with tart red ginger dressing</p></div>
  <div class="salad salad-3"><div class="salad-head"><h3 class="salad-name">Chinese Chicken Salad</h3><span class="salad-price">10.50</span></div><p class="item-desc">Shredded lettuce, chicken breast,<br>scallions, carrots, toasted almonds,<br>browncrunchies, and white crunchies<br>with tart red ginger dressing</p></div>
</main>
</body>
</html>
```